Design a Form to Match a Web Page Design

I need to you a proposal to get this form (3 pages) https://www.quillbarnhaven.com/eforms/analise-de-financiamento-e-rentabilidade-copy/35/ and match with the design concept of my home page https://www.quillbarnhaven.com/

```html
<!DOCTYPE html>
<html lang="en">
<head>
<meta charset="utf-8">
<title>Financing and Profitability Form – Step Views</title>
<link href="https://fonts.googleapis.com/css2?family=Poppins:wght@500;600;700&family=Open+Sans:wght@400;600&display=swap" rel="stylesheet">
<style>
  :root{
    --bg:#f2f2f2;
    --panel:#ffffff;
    --sky:#15a0c0;
    --crimson:#d4204a;
    --teal-a:#22a7b4;
    --teal-b:#117c8a;
    --orange:#f47b20;
    --ink:#444;
    --title:#5a5a5a;
    --line:#dcdcdc;
    --accent:#1a98a8;
  }
  html,body{margin:0;padding:0;width:1200px;height:1155px;overflow:hidden;background:var(--bg);}
  .canvas{position:relative;width:1960px;height:1887px;transform:scale(0.61225);transform-origin:0 0;font-family:"Open Sans",sans-serif;color:var(--ink);}
  .panel{position:absolute;background:var(--panel);}
  .stepbar{position:absolute;background:var(--sky);height:90px;}
  .banner{position:absolute;background:var(--crimson);height:115px;color:#fff;text-align:center;}
  .banner h1{margin:24px 0 0;font:700 34px "Poppins",sans-serif;letter-spacing:.3px;}
  .banner p{margin:6px 0 0;font:400 20px "Poppins",sans-serif;}
  .step{position:absolute;top:38px;font:700 22px "Poppins",sans-serif;color:rgba(255,255,255,.55);transform:translateX(-50%);white-space:nowrap;}
  .step.on{color:#fff;}
  .dot{position:absolute;top:20px;width:8px;height:8px;border:2.5px solid rgba(255,255,255,.8);border-radius:50%;transform:translateX(-50%);}
  .dash{position:absolute;top:26px;border-top:2px dotted rgba(255,255,255,.6);}
  .box{position:absolute;border:1.5px solid var(--line);background:#fff;}
  .t{position:absolute;white-space:nowrap;font-size:17px;line-height:1;}
  .h{font:600 24px "Poppins",sans-serif;color:var(--title);}
  .r{text-align:right;}
  .red{color:var(--crimson);}
  .acc{color:var(--accent);font-size:23px;}
  .sl{position:absolute;height:3px;background:var(--line);}
  .sl i{position:absolute;top:-7px;width:10px;height:10px;border:3.5px solid var(--accent);border-radius:50%;background:#fff;}
  .bar{position:absolute;color:#fff;background:linear-gradient(90deg,var(--teal-a),var(--teal-b));}
  .bar .k{position:absolute;left:22px;top:50%;transform:translateY(-50%);font:500 17px "Poppins",sans-serif;line-height:1.15;}
  .bar .v{position:absolute;right:20px;top:50%;transform:translateY(-50%);font:500 25px "Poppins",sans-serif;}
  .hot{position:absolute;color:#fff;background:linear-gradient(90deg,var(--orange),var(--crimson));}
  .hot .k{position:absolute;left:36px;top:50%;transform:translateY(-50%);font:600 17px "Poppins",sans-serif;}
  .hot .v{position:absolute;right:26px;top:50%;transform:translateY(-50%);font:600 28px "Poppins",sans-serif;}
  .btn{position:absolute;width:174px;height:48px;border-radius:24px;color:#fff;font:600 18px "Poppins",sans-serif;text-align:center;line-height:48px;}
  .btn.prev{background:var(--teal-b);background:linear-gradient(90deg,#178f9e,#1a98a8);}
  .btn.next{background:var(--orange);}
  .chev{position:absolute;width:14px;height:14px;border-left:2px solid #aaa;border-top:2px solid #aaa;transform:rotate(45deg);}
  .cal{display:inline-block;width:11px;height:11px;border:1.5px solid #999;border-top-width:3px;margin-right:3px;vertical-align:-1px;}
</style>
</head>
<body>
<div class="canvas">

  <!-- STEP 1: Property Financing -->
  <section class="panel" style="left:79px;top:55px;width:890px;height:850px;">
    <div class="stepbar" style="left:0;top:0;width:890px;">
      <span class="dot" style="left:233px"></span><span class="dash" style="left:246px;width:180px"></span>
      <span class="dot" style="left:438px"></span><span class="dash" style="left:451px;width:178px"></span>
      <span class="dot" style="left:639px"></span>
      <span class="step on" style="left:236px">STEP 01</span>
      <span class="step" style="left:442px">STEP 02</span>
      <span class="step" style="left:641px">STEP 03</span>
    </div>
    <div class="banner" style="left:0;top:90px;width:890px;"><h1>PROPERTY FINANCING</h1><p>Todos os valores apresentados em estão em Dólares Americanos</p></div>
  </section>
  <div class="box" style="left:97px;top:286px;width:853px;height:523px;"></div>
  <span class="t h" style="left:124px;top:336px">Property Financing</span>
  <span class="t" style="left:127px;top:390px">Property Value</span>
  <span class="t red" style="left:124px;top:426px;font-size:19px">$</span>
  <div class="sl" style="left:152px;top:434px;width:320px"><i style="left:-8px"></i></div>
  <span class="t" style="left:478px;top:428px">0</span>
  <span class="t" style="left:127px;top:489px">Entry (%) *</span>
  <span class="t red" style="left:124px;top:523px;font-size:19px">30</span>
  <div class="sl" style="left:158px;top:530px;width:320px"><i style="left:-8px"></i></div>
  <span class="t" style="left:126px;top:568px">Term (Years) *</span>
  <span class="t red" style="left:126px;top:602px;font-size:19px">30</span>
  <div class="sl" style="left:160px;top:609px;width:320px"><i style="left:-8px"></i></div>
  <span class="t" style="left:126px;top:650px">Input Value</span><span class="t" style="left:447px;top:650px">$ 0.00</span>
  <span class="t" style="left:126px;top:692px">Funded Amount</span><span class="t" style="left:447px;top:692px">$ 0.00</span>
  <span class="t" style="left:529px;top:407px">Financing Rate (Annual)</span>
  <span class="t red" style="left:529px;top:443px;font-size:19px">%</span>
  <div class="sl" style="left:557px;top:451px;width:320px"><i style="left:-8px"></i></div>
  <span class="t" style="left:883px;top:444px">5.75</span>
  <div class="bar" style="left:518px;top:482px;width:412px;height:52px;"><span class="k">Installment Value</span><span class="v">$0.00</span></div>
  <span class="t" style="left:533px;top:570px">Safe</span><span class="t" style="left:867px;top:570px">$ 0.00</span>
  <span class="t" style="left:533px;top:620px">Property Fees</span><span class="t" style="left:867px;top:620px">$ 0.00</span>
  <div class="hot" style="left:97px;top:752px;width:854px;height:57px;"><span class="k">TOTAL MONTHLY VALUE</span><span class="v">$0.00</span></div>
  <div class="btn prev" style="left:361px;top:838px">Previous</div>
  <div class="btn next" style="left:550px;top:838px">Next</div>

  <!-- STEP 2: Deed and Furniture Costs -->
  <section class="panel" style="left:79px;top:961px;width:890px;height:804px;">
    <div class="stepbar" style="left:0;top:0;width:883px;">
      <span class="dot" style="left:226px"></span><span class="dash" style="left:246px;width:180px"></span>
      <span class="dot" style="left:431px"></span><span class="dash" style="left:448px;width:180px"></span>
      <span class="dot" style="left:639px"></span>
      <span class="step" style="left:228px">STEP 01</span>
      <span class="step on" style="left:435px">STEP 02</span>
      <span class="step" style="left:641px">STEP 03</span>
    </div>
    <div class="banner" style="left:0;top:90px;width:883px;"><h1>DEED AND FURNITURE COSTS</h1><p>Todos os valores apresentados em estão em Dólares Americanos</p></div>
  </section>
  <div class="box" style="left:103px;top:1188px;width:413px;height:421px;"></div>
  <span class="t h" style="left:134px;top:1224px">Expenses in Deed</span><span class="chev" style="left:461px;top:1236px"></span>
  <span class="t" style="left:132px;top:1297px">Bank Costs / Financing</span><span class="t" style="left:444px;top:1297px">$0.00</span>
  <span class="t" style="left:132px;top:1346px">Expenses with Notary / Escrow</span><span class="t" style="left:447px;top:1350px">$0.00</span>
  <span class="t" style="left:132px;top:1395px">Incentive</span><span class="t" style="left:443px;top:1412px">-5000</span>
  <span class="t red" style="left:129px;top:1429px;font-size:19px">$</span>
  <div class="sl" style="left:152px;top:1436px;width:332px"><i style="left:-8px"></i></div>
  <span class="t" style="left:131px;top:1474px">Fees and Licenses</span><span class="t" style="left:414px;top:1472px">$1,330.00</span>
  <span class="t red" style="left:131px;top:1508px;font-size:19px">30</span>
  <div class="hot" style="left:103px;top:1559px;width:414px;height:50px;"><span class="k" style="left:28px">Total Closing</span><span class="v" style="right:22px;font-size:25px">$ -3,670.00</span></div>
  <div class="box" style="left:531px;top:1188px;width:420px;height:172px;"></div>
  <span class="t h" style="left:556px;top:1223px">Property Furniture</span><span class="chev" style="left:900px;top:1236px"></span>
  <span class="t" style="left:556px;top:1291px">Approximate Furniture Cost</span><span class="t acc" style="left:856px;top:1287px">$ 0.00</span>
  <div class="box" style="left:531px;top:1373px;width:420px;height:236px;"></div>
  <span class="t h" style="left:556px;top:1388px">Total investment</span><span class="chev" style="left:900px;top:1405px"></span>
  <div class="bar" style="left:547px;top:1445px;width:388px;height:52px;"><span class="k">Initial investment</span><span class="v">$ -3,670.00</span></div>
  <div class="btn prev" style="left:353px;top:1673px">Previous</div>
  <div class="btn next" style="left:542px;top:1673px">Next</div>

  <!-- STEP 3: Revenue, Expenses and Balance -->
  <section class="panel" style="left:1020px;top:55px;width:888px;height:1626px;">
    <div class="stepbar" style="left:0;top:0;width:888px;">
      <span class="dot" style="left:224px"></span><span class="dash" style="left:244px;width:180px"></span>
      <span class="dot" style="left:429px"></span><span class="dash" style="left:446px;width:180px"></span>
      <span class="dot" style="left:638px"></span>
      <span class="step" style="left:226px">STEP 01</span>
      <span class="step" style="left:433px">STEP 02</span>
      <span class="step on" style="left:640px">STEP 03</span>
    </div>
    <div class="banner" style="left:0;top:90px;width:888px;"><h1>DEED AND FURNITURE COSTS</h1><p>Todos os valores apresentados em estão em Dólares Americanos</p></div>
  </section>

  <div class="box" style="left:1043px;top:283px;width:413px;height:431px;"></div>
  <span class="t h" style="left:1072px;top:312px">Recipe</span><span class="chev" style="left:1401px;top:320px"></span>
  <span class="t" style="left:1072px;top:373px">Daily Rate</span>
  <span class="t red" style="left:1071px;top:402px;font-size:19px">$</span>
  <div class="sl" style="left:1099px;top:409px;width:288px"><i style="left:-8px"></i></div>
  <span class="t" style="left:1403px;top:404px">0</span>
  <span class="t" style="left:1072px;top:447px">Annual Occupancy Rate (%)</span>
  <span class="t red" style="left:1072px;top:483px;font-size:19px">73</span>
  <div class="sl" style="left:1097px;top:490px;width:290px"><i style="left:173px"></i></div>
  <span class="t" style="left:1395px;top:483px">73%</span>
  <span class="t" style="left:1069px;top:533px">Days of busy year</span><span class="t" style="left:1384px;top:532px"><span class="cal"></span>266</span>
  <span class="t" style="left:1069px;top:582px">Vacant year days</span><span class="t" style="left:1384px;top:579px"><span class="cal"></span>99</span>
  <div class="bar" style="left:1058px;top:638px;width:384px;height:50px;"><span class="k">Gross Revenue</span><span class="v">$0.00</span></div>

  <div class="box" style="left:1043px;top:725px;width:413px;height:215px;"></div>
  <span class="t h" style="left:1072px;top:755px">Adm Commission (20%)</span><span class="chev" style="left:1401px;top:764px"></span>
  <span class="t" style="left:1072px;top:809px">Adm.</span><span class="t" style="left:1384px;top:811px">$0.00</span>
  <span class="t" style="left:1072px;top:837px;font-size:13.5px">Commission 20% (Under Gross Revenue)</span>
  <div class="bar" style="left:1058px;top:872px;width:384px;height:50px;"><span class="k" style="left:28px">Net Revenue</span><span class="v">$0.00</span></div>

  <div class="box" style="left:1470px;top:283px;width:420px;height:657px;"></div>
  <span class="t h" style="left:1493px;top:310px;font-size:20px;line-height:1.25">Amortization Financing<br>and Amount Invested</span><span class="chev" style="left:1840px;top:330px"></span>
  <span class="t" style="left:1493px;top:403px;line-height:1.4">Financing Portion<br>(12 months)</span><span class="t" style="left:1820px;top:404px">$0.00</span>
  <span class="t" style="left:1492px;top:481px">Initial investment</span><span class="t" style="left:1798px;top:482px">$3,670.00</span>
  <span class="t" style="left:1493px;top:546px;line-height:1.4">ROI (Profitability<br>/ Investment)</span><span class="t acc" style="left:1781px;top:541px">327.52 %</span>
  <span class="t" style="left:1492px;top:622px">Debt amortization</span><span class="t acc" style="left:1781px;top:617px">$ 0.00</span>
  <span class="t" style="left:1493px;top:695px">Amortization ROI</span><span class="t acc" style="left:1781px;top:691px">327.52 %</span>

  <div class="box" style="left:1043px;top:954px;width:847px;height:466px;"></div>
  <span class="t h" style="left:1072px;top:987px;font-size:21px">Fixed Property Expenses</span><span class="chev" style="left:1402px;top:992px"></span>
  <span class="t" style="left:1072px;top:1026px">HOA ((Owners Association Fee) 12 months)</span>
  <span class="t red" style="left:1078px;top:1055px">$</span><span class="t" style="left:1375px;top:1056px">4200</span>
  <div class="sl" style="left:1084px;top:1081px;width:332px"><i style="left:-8px"></i></div>
  <span class="t" style="left:1073px;top:1112px">Adm Rate + Licenses (12 months)</span>
  <span class="t red" style="left:1075px;top:1140px">$</span><span class="t" style="left:1372px;top:1141px">1800</span>
  <div class="sl" style="left:1081px;top:1165px;width:332px"><i style="left:-8px"></i></div>
  <span class="t" style="left:1074px;top:1201px">Swimming Pool (12 months)</span>
  <span class="t red" style="left:1076px;top:1229px">$</span><span class="t" style="left:1373px;top:1230px">960</span>
  <div class="sl" style="left:1082px;top:1255px;width:332px"><i style="left:-8px"></i></div>
  <span class="t" style="left:1075px;top:1296px">Light / Water / Gas (12 months)</span>
  <span class="t red" style="left:1077px;top:1323px">$</span><span class="t" style="left:1374px;top:1324px">3480</span>
  <div class="sl" style="left:1083px;top:1349px;width:332px"><i style="left:-8px"></i></div>
  <span class="t" style="left:1518px;top:1063px">Maintenance (12 months)</span>
  <span class="t red" style="left:1520px;top:1091px">$</span><span class="t" style="left:1817px;top:1092px">1200</span>
  <div class="sl" style="left:1526px;top:1116px;width:332px"><i style="left:-8px"></i></div>
  <span class="t" style="left:1520px;top:1157px">Accounting (12 months)</span>
  <span class="t red" style="left:1522px;top:1185px">$</span><span class="t" style="left:1819px;top:1186px">380</span>
  <div class="sl" style="left:1528px;top:1210px;width:332px"><i style="left:-8px"></i></div>
  <div class="bar" style="left:1512px;top:1252px;width:368px;height:52px;"><span class="k" style="left:20px;font-size:16px">Fixed Property<br>Expenses (12 months)</span><span class="v" style="font-size:21px">$ -12,020.00</span></div>
  <div class="bar" style="left:1512px;top:1316px;width:368px;height:52px;"><span class="k" style="left:20px">Profitability</span><span class="v" style="font-size:21px">$ -12,020.00</span></div>

  <div class="hot" style="left:1046px;top:1432px;width:842px;height:116px;">
    <span class="k" style="left:37px;font-size:19px;line-height:1.3">Net Balance after paying the<br>financing installments</span>
    <span class="chev" style="left:346px;top:42px;border-color:rgba(255,255,255,.8)"></span>
    <span class="k" style="left:449px">Final Net Balance</span>
    <span class="v">$ -12,020.00</span>
  </div>
  <div class="btn prev" style="left:1286px;top:1573px">Previous</div>
  <div class="btn next" style="left:1476px;top:1573px">Next</div>

</div>
</body>
</html>
```